Bright Nest - Business Card

Modern Business Card : I like a simple, clean designs. Think Pearl!

Information to Include
Bright Nest Inc. (Logo)
Name: Tom Harker
Position: President
Office: 555-382-9146
Fax: 555-382-9146
Cell: 555-382-9146
E-Mail: tharker@thebrightnest.example
Website: www.thebrightnest.example

I attached the "guardlink.example" dealer logo. This logo is not a requirement, but a plus if it looks good with the design.

I also have access to more pictures and logos, if you see something on guardlink.example
or 3vox.example, I can probably get the file. Again, this is not mandatory.

```html
<!DOCTYPE html>
<html lang="en">
<head>
<meta charset="utf-8">
<title>Bright Nest – Business Card</title>
<link rel="stylesheet" href="https://fonts.googleapis.com/css2?family=Exo+2:wght@400;500;700&display=swap">
<style>
  :root {
    --orange: #e2622f;
    --ink: #111111;
    --paper: #ffffff;
    --paper-shade: #ececec;
    --backdrop: #d9d9d9;
    --muted: #333333;
  }
  * { box-sizing: border-box; margin: 0; padding: 0; }
  html, body { width: 1200px; height: 1022px; overflow: hidden; }
  body {
    background: var(--backdrop);
    font-family: "Exo 2", Arial, sans-serif;
    position: relative;
  }
  .card {
    position: absolute;
    width: 520px;
    height: 300px;
    border-radius: 26px;
    overflow: hidden;
    background: linear-gradient(135deg, var(--paper-shade) 0%, var(--paper) 55%);
    box-shadow: 0 6px 18px rgba(0,0,0,0.25);
  }
  .card-front { left: 60px; top: 361px; }
  .card-back { left: 620px; top: 361px; }
  .card-shapes { position: absolute; inset: 0; width: 520px; height: 300px; }

  .brand {
    position: absolute;
    display: flex;
    align-items: center;
    gap: 10px;
  }
  .brand-mark {
    width: 34px;
    height: 34px;
    background: var(--orange);
  }
  .brand-name {
    font-weight: 700;
    color: var(--ink);
    font-size: 34px;
    line-height: 1;
  }
  .card-front .brand { left: 30px; top: 150px; }
  .card-front .brand-name { font-size: 30px; }
  .card-front .brand-mark { width: 30px; height: 30px; }

  .person {
    position: absolute;
    left: 30px;
    top: 232px;
    padding-left: 14px;
    border-left: 5px solid var(--muted);
    color: var(--ink);
  }
  .person-name { font-size: 19px; font-weight: 500; letter-spacing: 1px; text-transform: uppercase; }
  .person-role { font-size: 14px; }

  .contact {
    position: absolute;
    left: 300px;
    top: 34px;
    width: 200px;
    color: var(--paper);
    font-size: 13px;
    line-height: 1.45;
  }
  .contact-address { margin-bottom: 14px; letter-spacing: 0.5px; }
  .contact-list { list-style: none; }
  .contact-list li { display: flex; align-items: center; justify-content: space-between; margin-bottom: 6px; }
  .contact-list svg { width: 14px; height: 14px; flex: none; }
  .contact-web { margin-top: 10px; font-size: 12px; }
  .contact-web p { white-space: nowrap; }

  .card-back .brand { left: 190px; top: 130px; }
  .back-web {
    position: absolute;
    left: 38px;
    top: 150px;
    transform: translate(-50%, -50%) rotate(-90deg);
    color: var(--paper);
    font-size: 14px;
    letter-spacing: 0.5px;
    white-space: nowrap;
  }
</style>
</head>
<body>

<section class="card card-front">
  <svg class="card-shapes" viewBox="0 0 520 300" aria-hidden="true">
    <path d="M292 0 Q178 150 292 300" fill="none" stroke="var(--ink)" stroke-width="6"/>
    <path d="M302 0 Q190 150 302 300 L520 300 L520 0 Z" fill="var(--orange)"/>
  </svg>

  <div class="brand">
    <span class="brand-mark"></span>
    <span class="brand-name">Bright Nest</span>
  </div>

  <div class="person">
    <p class="person-name">Tom Harker</p>
    <p class="person-role">President</p>
  </div>

  <div class="contact">
    <p class="contact-address">208, 4th floor, Elm Court<br>Harbor Road East</p>
    <ul class="contact-list">
      <li><span>555 382 9146</span>
        <svg viewBox="0 0 16 16"><path d="M3 1h3l1 4-2 1a9 9 0 0 0 5 5l1-2 4 1v3a2 2 0 0 1-2 2A13 13 0 0 1 1 3a2 2 0 0 1 2-2z" fill="var(--paper)"/></svg></li>
      <li><span>555 382 9146</span>
        <svg viewBox="0 0 16 16"><rect x="4" y="1" width="8" height="14" rx="1.5" fill="none" stroke="var(--paper)" stroke-width="1.6"/></svg></li>
      <li><span>555 382 9146</span>
        <svg viewBox="0 0 16 16"><rect x="2" y="6" width="12" height="8" fill="var(--paper)"/><rect x="4" y="2" width="8" height="4" fill="none" stroke="var(--paper)" stroke-width="1.4"/></svg></li>
    </ul>
    <div class="contact-web">
      <p>tharker@thebrightnest.example</p>
      <p>www.thebrightnest.example</p>
    </div>
  </div>
</section>

<section class="card card-back">
  <svg class="card-shapes" viewBox="0 0 520 300" aria-hidden="true">
    <path d="M0 0 L86 0 Q52 150 86 300 L0 300 Z" fill="var(--orange)"/>
    <path d="M92 0 Q58 150 92 300" fill="none" stroke="var(--ink)" stroke-width="5"/>
  </svg>

  <p class="back-web">www.thebrightnest.example</p>

  <div class="brand">
    <span class="brand-mark"></span>
    <span class="brand-name">Bright Nest</span>
  </div>
</section>

</body>
</html>
```